Buch-/eBook-Cover für ein Fantasy Roman
Zielgruppe
Meine Zielgruppe sind Jugendliche und junge Erwachsene, aber auch für Ältere könnte mein Buch interessant sein.
Aufgabenstellung
Bei meinem Buch handelt es sich um einen Fantasy Roman. Es heißt 'Nachtfalter - Wahrheit braucht ihre Zeit' und der Autor ist Mara Oswaldtinger.
Das Buch handelt von einem Mädchen, welches eigentlich ein ganz normales Leben führt, aber dieses durch eine Pressekonferenz vom Präsidenten komplett durcheinander gerät. Denn viele Menschen sollen an einem Virus leiden. Die Menschen sollen sich aber keine Sorgen machen. Doch alles läuft durcheinander, da die infizierten Menschen einer nach dem anderen spurlos verschwinden.
Auf meinem Cover soll keine Figur zu sehen sein. Ich hätte gerne ein Zusammenspiel zwischen den Farben Blau und Grün. sie sollen harmonisch und fließend ineinander übergehen. Auch etwas Glitzer für etwas Geheimnisvolles darf auf dem Cover sein. Den Titel hätte ich gerne in der Mitte. Wo der Autorname stehen soll, bin ich offen.

```html
<!DOCTYPE html>
<html lang="de">
<head>
<meta charset="utf-8">
<title>Nachtfalter – Buchumschlag</title>
<link rel="stylesheet" href="https://fonts.googleapis.com/css2?family=Cinzel:wght@400;600;700&family=EB+Garamond:wght@400&display=swap">
<style>
  :root {
    --ink-deep: #04141c;
    --teal-dark: #0b3a44;
    --teal: #1d7d86;
    --teal-bright: #35b6b4;
    --blue-deep: #0a2748;
    --gold-light: #f5dcae;
    --gold: #c99a5b;
    --gold-dark: #7a5429;
    --text-light: #f2f1ec;
    --author-cyan: #2fb3d0;
    --author-front: #2e93a8;
    --code-box: #ffffff;
  }
  * { margin: 0; padding: 0; box-sizing: border-box; }
  html, body { width: 1200px; height: 888px; overflow: hidden; background: var(--ink-deep); }
  .cover-wrap { position: relative; width: 1200px; height: 888px; overflow: hidden; }

  .cover-artwork {
    position: absolute; inset: 0;
    background:
      radial-gradient(ellipse 260px 200px at 120px 60px, rgba(53,182,180,.55), transparent 70%),
      radial-gradient(ellipse 300px 260px at 1080px 120px, rgba(29,125,134,.55), transparent 70%),
      radial-gradient(ellipse 240px 300px at 330px 640px, rgba(53,160,170,.55), transparent 70%),
      radial-gradient(ellipse 240px 300px at 880px 660px, rgba(53,160,170,.55), transparent 70%),
      radial-gradient(ellipse 200px 160px at 60px 560px, rgba(20,80,140,.5), transparent 70%),
      radial-gradient(ellipse 200px 160px at 1150px 560px, rgba(20,80,140,.5), transparent 70%),
      radial-gradient(ellipse 160px 120px at 600px 470px, rgba(29,125,134,.45), transparent 70%),
      radial-gradient(ellipse 220px 140px at 430px 860px, rgba(40,130,110,.45), transparent 70%),
      radial-gradient(ellipse 220px 140px at 960px 860px, rgba(40,130,110,.45), transparent 70%),
      linear-gradient(180deg, var(--teal-dark) 0%, var(--ink-deep) 45%, var(--blue-deep) 75%, var(--ink-deep) 100%);
  }

  .back-blurb {
    position: absolute; left: 63px; top: 74px; width: 434px;
    font-family: "EB Garamond", serif; font-size: 22px; line-height: 25.4px;
    color: var(--text-light); text-align: justify;
    text-shadow: 0 1px 3px rgba(0,0,0,.6);
  }

  .code-box {
    position: absolute; left: 344px; top: 730px; width: 201px; height: 118px;
    background: var(--code-box);
  }

  .gold-type {
    background: linear-gradient(180deg, var(--gold-light) 0%, var(--gold) 50%, var(--gold-dark) 80%, var(--gold) 100%);
    -webkit-background-clip: text; background-clip: text; color: transparent;
    filter: drop-shadow(0 2px 3px rgba(0,0,0,.6));
  }

  .spine-line {
    position: absolute; left: 600px; white-space: nowrap;
    transform-origin: 0 0; transform: rotate(90deg) translateY(-50%);
  }
  .spine-title { top: 74px; font-family: "Cinzel", serif; font-weight: 600; font-size: 22px; letter-spacing: 0.5px; }
  .spine-title .initial { font-size: 28px; }
  .spine-subtitle { top: 286px; font-family: "Cinzel", serif; font-size: 15px; color: var(--text-light); }
  .spine-author { top: 576px; font-family: "Cinzel", serif; font-size: 22px; letter-spacing: 1px; color: var(--author-cyan); }

  .front-title {
    position: absolute; left: 660px; width: 520px; top: 340px; text-align: center;
    font-family: "Cinzel", serif; font-weight: 700; font-size: 52px; white-space: nowrap; line-height: 1;
  }
  .front-title .initial { font-size: 74px; }
  .front-subtitle {
    position: absolute; left: 660px; width: 520px; top: 482px; text-align: center;
    font-family: "Cinzel", serif; font-size: 27px; color: var(--text-light); white-space: nowrap;
    text-shadow: 0 1px 4px rgba(0,0,0,.7);
  }
  .front-author {
    position: absolute; left: 660px; width: 520px; top: 818px; text-align: center;
    font-family: "Cinzel", serif; font-size: 29px; color: var(--author-front); white-space: nowrap;
  }
</style>
</head>
<body>
<main class="cover-wrap">
  <div class="cover-artwork" role="img" aria-label="Fließender Rauch in Blau- und Grüntönen, gespiegelt, mit goldenem Glitzer auf dunklem Grund"></div>

  <section class="back-cover">
    <p class="back-blurb">Lorem ipsum dolor sit amet, consetetur sadipscing elitr, sed diam nonumy eirmod tempor invidunt ut labore et dolore magna aliquyam erat, sed diam voluptua. At vero eos et accusam et justo duo dolores et ea rebum. Stet clita kasd gubergren, no sea takimata sanctus est Lorem ipsum dolor sit amet. Lorem ipsum dolor sit amet, consetetur sadipscing elitr, sed diam nonumy eirmod tempor invidunt ut labore et dolore magna aliquyam erat, sed diam voluptua. At vero eos et accusam et justo duo dolores et ea rebum. Stet clita kasd gubergren, no sea takimata sanctus est Lorem ipsum dolor sit amet.</p>
    <div class="code-box"></div>
  </section>

  <section class="spine">
    <div class="spine-line spine-title gold-type"><span class="initial">N</span>ACHTFALTE<span class="initial">R</span></div>
    <div class="spine-line spine-subtitle">WAHRHEIT BRAUCHT IHRE ZEIT</div>
    <div class="spine-line spine-author">MARA OSWALDTINGER</div>
  </section>

  <section class="front-cover">
    <h1 class="front-title gold-type"><span class="initial">N</span>ACHTFALTE<span class="initial">R</span></h1>
    <p class="front-subtitle">WAHRHEIT BRAUCHT IHRE ZEIT</p>
    <p class="front-author">MARA OSWALDTINGER</p>
  </section>
</main>
</body>
</html>
```